Quill Pet Shop Homepage

We are a pet shop, we focus on dog food / cat food / rodents & bird food

Based on WooCommerce

It should be a simple but professional homepage with an informative start page. In the shop it should then be possible to shop for products/manufacturers etc. Navigation/Filter menu on the left would be ideal.

Next menus:
ABOUT US
CONTACT
DOG
CAT
HOLDER

My Account - Login
My Cart

Footer:
Conditions
payment options
social media

In addition to our logo, I have attached 2 example pages from another shop which we would use as a guideline.

Target Market(s)

pet store

Industry/Entity Type

Animal, Pet Shop

Coding

Coded - Design and coding required

Number of Pages Required

1 page

Font styles to use
Sans Serif

Colors
0054AA
0677BA
7BADD7
CADEEF
E8F1F8

Requirements
Must have
• Main Page, Contact, About Us, Shop, Check Out, Member Login, Mailchimp Marketing - We work with WooCommerce

```html
<!DOCTYPE html>
<html lang="en">
<head>
<meta charset="utf-8">
<title>Quill Pet Shop – Premium Pet Food</title>
<link href="https://fonts.googleapis.com/css2?family=Fira+Sans:wght@400;500;600;700&family=Roboto:wght@400;500;700&display=swap" rel="stylesheet">
<style>
:root{
  --blue:#0054AA;
  --blue-2:#0677BA;
  --blue-3:#7BADD7;
  --blue-4:#CADEEF;
  --blue-5:#E8F1F8;
  --navy:#0b1a30;
  --ink:#1c2430;
  --text:#3d4652;
  --muted:#8a929c;
  --line:#e2e6ea;
  --about:#2373b6;
}
*{box-sizing:border-box;margin:0;padding:0}
html,body{width:1200px;height:3363px;overflow:hidden;background:#fff}
body{font-family:"Roboto",sans-serif;color:var(--text);font-size:13px}
.page{position:relative;width:1200px;height:3363px;overflow:hidden}
.abs{position:absolute}
h1,h2,h3,h4,.fira{font-family:"Fira Sans",sans-serif}
.blue{color:var(--blue)}
.btn{display:inline-flex;align-items:center;gap:8px;background:var(--blue);color:#fff;border-radius:3px;font-size:12px;padding:0 10px;height:26px}
.btn svg{width:16px;height:16px}
.strike{text-decoration:line-through;color:var(--muted)}
.img{border-radius:4px}

/* top bar */
.topbar{top:0;left:0;width:1200px;height:21px;background:var(--navy);color:#cfd7e2;font-size:11px;text-align:center;line-height:21px}

/* header */
.brand{display:flex;align-items:center;gap:10px}
.brand .dot{width:44px;height:44px;border-radius:50%;background:var(--blue)}
.brand span{font-family:"Fira Sans",sans-serif;font-weight:700;font-size:22px;color:var(--blue)}
.mainnav{top:42px;left:447px;display:flex;gap:28px;font-size:11.5px;color:var(--ink)}
.subnav{top:42px;left:916px;display:flex;gap:20px;font-size:11.5px;color:var(--ink)}
.lang{top:42px;left:1072px;font-size:11.5px;color:var(--blue)}
.lang b{font-weight:400;color:var(--muted)}
.shopcat{top:85px;left:306px;font-size:12px;color:var(--ink)}
.search{top:74px;left:422px;width:499px;height:33px;border:1px solid #cfd5dc;border-radius:3px;display:flex;align-items:center}
.search .q{flex:1;display:flex;align-items:center;gap:8px;padding-left:12px;color:#a0a7b0;font-size:12px}
.search .cat{width:124px;height:100%;border-left:1px solid #cfd5dc;display:flex;align-items:center;justify-content:space-between;padding:0 12px 0 20px;font-size:11.5px;color:var(--text)}
.cart{top:80px;left:945px}
.login{top:74px;left:1003px;width:46px;height:33px;background:var(--blue);color:#fff;border-radius:3px;font-size:12px;display:flex;align-items:center;justify-content:center}
.register{top:74px;left:1057px;width:60px;height:33px;background:#0f1c2e;color:#fff;border-radius:3px;font-size:12px;display:flex;align-items:center;justify-content:center}

/* hero */
.hero-main{top:148px;left:84px;width:593px;height:344px;background:linear-gradient(90deg,#eef1f6,#e6ebf2);border-radius:4px;overflow:hidden}
.hero-main .photo{position:absolute;right:0;top:0;width:232px;height:344px;background:linear-gradient(160deg,#f4f4f4 0%,#e9b97c 45%,#c9773a 70%,#d63a2e 100%)}
.disc{position:absolute;width:68px;height:68px;border-radius:50%;background:var(--blue);color:#fff;text-align:center;font-family:"Fira Sans",sans-serif}
.disc b{display:block;font-size:18px;margin-top:18px;line-height:1}
.disc small{font-size:7px;letter-spacing:.5px}
.eyebrow{font-family:"Fira Sans",sans-serif;font-size:11px;font-weight:600;letter-spacing:.6px;color:var(--blue)}
.hero-main h1{font-size:37px;font-weight:500;color:var(--ink)}
.hero-main p{font-size:11.5px;line-height:18px;color:#59626e;width:322px}
.price-lg{font-family:"Fira Sans",sans-serif;font-size:19px;color:var(--blue)}
.price-lg .strike{margin-left:16px;color:#6b7380}
.dots{display:flex;gap:9px}
.dots i{width:7px;height:7px;border-radius:50%;background:#c8cfd8}
.dots i.on{background:var(--blue)}

.hero-side{left:697px;width:420px;height:162px;border-radius:4px;overflow:hidden}
.hero-side h3{position:absolute;left:40px;top:30px;width:230px;font-size:22px;font-weight:500;line-height:28px;color:var(--ink)}
.hero-side .eyebrow{position:absolute;left:40px;top:97px;color:#394352;font-weight:500}
.hero-side .pr{position:absolute;left:40px;top:124px;font-family:"Fira Sans",sans-serif;font-size:15px;color:var(--blue)}
.hero-side .pack{position:absolute;right:34px;top:18px;width:74px;height:128px;border-radius:6px}
.pct{position:absolute;background:var(--blue);color:#fff;font-size:11px;font-weight:700;padding:3px 8px;border-radius:3px}

/* special band */
.special{top:539px;left:81px;width:1036px;height:101px;border-radius:50px;background:linear-gradient(90deg,#e6f1fb,#bfe0f8)}
.special h2{position:absolute;left:43px;top:24px;font-size:25px;font-weight:500;color:#1f2d40}
.special h2 em{font-style:normal;color:var(--blue-2)}
.special p{position:absolute;left:43px;top:62px;font-size:11.5px;color:#4b5562}
.special .cans{position:absolute;left:761px;top:-32px;width:230px;height:133px;border-radius:8px;background:linear-gradient(120deg,#f3d7a4,#c4382c 45%,#8b2a1e 70%,#3d5ea8)}

/* filter */
.filter{top:676px;left:84px;width:242px}
.filter .head{display:flex;justify-content:space-between;align-items:center;font-size:15px;color:#2a323c}
.filter h3{font-size:20px;font-weight:500;color:var(--ink);margin-top:30px}
.slider{position:relative;height:4px;background:#d9dde2;border-radius:2px;margin-top:22px}
.slider .fill{position:absolute;left:0;top:0;height:4px;width:121px;background:var(--blue);border-radius:2px}
.slider .knob{position:absolute;left:114px;top:-7px;width:18px;height:18px;border-radius:50%;background:var(--blue)}
.range{display:flex;justify-content:space-between;font-size:10.5px;color:#a6adb6;margin-top:13px}
.range b{font-weight:500;color:var(--ink);font-size:11px}
.cats{list-style:none;margin-top:14px;font-size:15px;color:#2a323c}
.cats li{line-height:29px}
.cats li.on{color:var(--blue)}
.cats ul{list-style:none;padding-left:26px;font-size:12.5px;color:#3a4350}
.cats ul li{line-height:26px}

/* product grid */
.pcard{width:217px;height:237px;border:1px solid #dfe3e8;border-radius:6px;background:#fff}
.pcard .new{position:absolute;left:18px;top:16px;background:var(--blue);color:#fff;font-size:9px;font-weight:700;padding:3px 6px;border-radius:3px}
.heart{position:absolute;width:26px;height:26px;border-radius:50%;border:1px solid #d5dbe2;display:flex;align-items:center;justify-content:center}
.heart svg{width:12px;height:12px}
.pcard .heart{right:16px;top:15px}
.pcard .pack{position:absolute;left:78px;top:26px;width:62px;height:98px;border-radius:5px}
.pcard .stars{position:absolute;left:0;width:100%;top:130px;text-align:center;color:var(--blue);font-size:11px;letter-spacing:1px}
.pcard .name{position:absolute;left:0;width:100%;top:149px;text-align:center;font-size:11.5px;color:#2a323c}
.pcard .pp{position:absolute;left:0;width:100%;top:174px;text-align:center;font-size:12px;color:var(--blue)}
.pcard .pp .strike{margin-left:14px;color:#6b7380}
.pcard .btn{position:absolute;left:55px;top:199px;height:22px;font-size:11px}
.pager{top:1199px;left:673px;display:flex;gap:9px}
.pager span{width:28px;height:28px;border:1px solid #cfd5dc;border-radius:3px;display:flex;align-items:center;justify-content:center;font-size:11.5px;color:var(--ink)}
.pager .prev{background:#c0c6ce;border-color:#c0c6ce}
.pager .cur{border-color:var(--blue);color:var(--blue)}

/* offers */
.tabs{top:1317px;left:84px;width:1033px;height:32px;border-bottom:2px solid #e1e5ea;display:flex;align-items:flex-start;font-size:12.5px;color:#2a323c}
.tabs .t{display:flex;align-items:center;gap:7px;padding-right:22px;margin-right:22px}
.tabs .t.sep{border-right:1px solid #cfd5dc}
.tabs .t.b{color:var(--blue)}
.tabs .see{margin-left:auto;display:flex;gap:22px;font-size:15px;font-weight:500;color:#2a323c}
.offer{border-radius:4px;overflow:hidden}
.offer .ph{position:absolute;inset:0}
.offer .shade{position:absolute;inset:0;background:linear-gradient(180deg,rgba(0,0,0,0) 40%,rgba(0,0,0,.55))}
.tag{display:inline-block;background:var(--blue);color:#fff;font-family:"Fira Sans",sans-serif;font-size:11px;font-weight:500;letter-spacing:.5px;padding:2px 4px}
.offer h3{color:#fff;font-weight:500;line-height:1.15}
.offer .op{color:#fff;font-family:"Fira Sans",sans-serif}

/* brands */
.brands{top:1839px;left:0;width:1200px;height:376px;background:var(--blue-5)}
.brands h2{position:absolute;top:40px;width:100%;text-align:center;font-size:37px;font-weight:500;color:#2a323c}
.brands .sub{position:absolute;top:94px;width:100%;text-align:center;font-size:12.5px;font-weight:500;color:#2a323c}
.bgrid{position:absolute;left:84px;top:143px;width:1033px;display:grid;grid-template-columns:repeat(5,1fr)}
.bgrid div{height:93px;display:flex;align-items:center;justify-content:center;font-family:"Fira Sans",sans-serif;font-weight:600;font-size:22px;color:#24344d;border-right:1px solid #d5dde7}
.bgrid div:nth-child(5n){border-right:none}
.bgrid div:nth-child(-n+5){border-bottom:1px solid #d5dde7}

/* deals */
.dhead{top:2260px;left:84px;width:1033px;height:40px;border-bottom:2px solid #e1e5ea;display:flex;justify-content:space-between;font-size:15px;font-weight:500;color:#2a323c}
.dhead .see{display:flex;gap:22px}
.dcard{top:2331px;width:155px;height:246px;border:1px solid #dfe3e8;border-radius:6px;background:#fff}
.dcard .heart{right:14px;top:14px}
.dcard .pack{position:absolute;left:44px;top:18px;width:64px;height:108px;border-radius:5px}
.dcard .name{position:absolute;left:13px;top:136px;width:135px;font-size:12px;line-height:16px;color:#2a323c}
.dcard .pp{position:absolute;left:13px;top:180px;font-size:13px;color:var(--blue)}
.dcard .pp .strike{margin-left:16px;color:#6b7380}
.dcard .off{position:absolute;left:13px;top:210px;background:var(--blue-5);color:var(--blue);font-size:9.5px;font-weight:700;letter-spacing:.6px;padding:3px 7px;border-radius:9px}
.arrow{top:2437px;width:36px;height:36px;border-radius:50%;background:#fff;box-shadow:0 2px 8px rgba(0,0,0,.15);display:flex;align-items:center;justify-content:center}

/* about */
.about{top:2663px;left:84px;width:1033px;height:347px;background:var(--about);border-radius:6px}
.about .video{position:absolute;left:37px;top:37px;width:439px;height:276px;border-radius:4px;background:linear-gradient(135deg,#3a6fb5 0%,#c9d3de 40%,#e9e6df 60%,#b39278 100%)}
.play{position:absolute;left:190px;top:108px;width:60px;height:60px;border-radius:50%;background:var(--blue);display:flex;align-items:center;justify-content:center}
.about h2{position:absolute;left:561px;top:52px;font-size:39px;font-weight:500;color:#fff}
.about p{position:absolute;left:561px;top:116px;width:382px;font-size:13px;line-height:22px;color:#d5e5f4}
.about .more{position:absolute;left:561px;top:264px;height:31px;padding:0 8px;border:1px solid #bcd6ee;border-radius:3px;color:#fff;font-size:12px;display:flex;align-items:center}

/* footer */
.fcontact{top:3163px;left:84px;width:210px;font-size:11.5px;color:#2a323c}
.fcontact .row{display:flex;gap:10px;align-items:flex-start;margin-bottom:20px;line-height:15px}
.fcontact svg{flex:none;width:16px;height:16px;margin-top:-1px}
.fcol{top:3100px}
.fcol h4{font-size:16px;font-weight:500;color:#2a323c;margin-bottom:10px}
.fcol a{display:block;font-size:12.5px;color:#3a4350;line-height:21.6px;text-decoration:none}
.pay{display:flex;gap:12px;font-family:"Fira Sans",sans-serif;font-weight:600;font-size:13px;color:#1f3b73;margin-bottom:28px}
.social{display:flex;gap:12px;font-size:13px;color:var(--blue)}
.copy{top:3310px;left:84px;width:1033px;border-top:1px solid #e1e5ea;padding-top:14px;font-size:12px;color:#3a4350}
</style>
</head>
<body>
<div class="page">

  <div class="abs topbar">Save time and money &nbsp;with QUILL PET PREMIUM PET FOOD</div>

  <!-- header -->
  <div class="abs brand" style="top:40px;left:84px"><i class="dot"></i><span>Quill Pet Shop</span></div>
  <nav class="abs mainnav"><span>ABOUT US</span><span>CONTACT</span><span>DOG</span><span>CAT</span><span>HOLDER</span></nav>
  <div class="abs subnav"><span>Watchlist ˅</span><span>Product ˅</span></div>
  <div class="abs lang">Eng <b>| De</b></div>
  <div class="abs shopcat">Shop by Category</div>
  <div class="abs search">
    <div class="q"><svg width="12" height="12" viewBox="0 0 12 12" fill="none" stroke="#a0a7b0" stroke-width="1.4"><circle cx="5" cy="5" r="4"/><path d="M8 8l3 3"/></svg>Search for anything</div>
    <div class="cat">All Category <svg width="9" height="6" viewBox="0 0 9 6" fill="none" stroke="#8a929c"><path d="M1 1l3.5 3.5L8 1"/></svg></div>
  </div>
  <svg class="abs cart" width="22" height="20" viewBox="0 0 22 20" fill="none" stroke="#2a323c" stroke-width="1.6"><path d="M2 7h16l-2 10H4z"/><path d="M6 7l3-5M14 7l-3-5"/><circle cx="17" cy="4" r="4" fill="#0054AA" stroke="none"/></svg>
  <div class="abs login">Login</div>
  <div class="abs register">Register</div>

  <!-- hero -->
  <section class="abs hero-main">
    <div class="photo" role="img" aria-label="Cat beside a bag of dry cat food and a red food bowl"></div>
    <div class="disc" style="left:40px;top:11px"><b>20%</b><small>DISCOUNT</small></div>
    <div class="eyebrow abs" style="left:40px;top:93px">ALIQUET PORTTITOR NISL</div>
    <h1 class="abs" style="left:40px;top:112px">Natural Cat Treats</h1>
    <p class="abs" style="left:40px;top:166px">Lorem ipsum dolor sit amet consectetur. Aliquet porttitor nisl id eu quam etiam. Sem sit sed maecenas enim tellus vel proin. Viverra leo aliquet sit pharetra viverra nisi.</p>
    <div class="price-lg abs" style="left:40px;top:242px">£ 4.49 <span class="strike">£ 7.99</span></div>
    <span class="btn abs" style="left:40px;top:280px;height:32px">Add to Cart <svg viewBox="0 0 16 16" fill="none" stroke="#fff" stroke-width="1.3"><path d="M1 2h2l2 8h8l2-6H4"/><circle cx="6" cy="13" r="1"/><circle cx="12" cy="13" r="1"/></svg></span>
    <div class="dots abs" style="left:225px;top:318px"><i class="on"></i><i></i><i></i><i></i></div>
  </section>

  <section class="abs hero-side" style="top:148px;background:#e3f6e6">
    <h3>Free-Run Chicken Wet Cat Food</h3>
    <div class="eyebrow">ALIQUET PORTTITOR NISL</div>
    <div class="pr">£ 5.99</div>
    <div class="pack" role="img" aria-label="Bag of dog food" style="background:linear-gradient(180deg,#2d3d5a,#c9ccd6 60%,#e8eaf0)"></div>
    <div class="pct" style="right:12px;top:14px">15%</div>
  </section>
  <section class="abs hero-side" style="top:330px;background:#fbe4f7">
    <h3>Free-Run Chicken Wet Cat Food</h3>
    <div class="eyebrow">ALIQUET PORTTITOR NISL</div>
    <div class="pr">£ 8.29</div>
    <div class="pack" role="img" aria-label="Pouch of wet cat food" style="background:linear-gradient(180deg,#1d56b8,#2c74d8 50%,#e8edf6)"></div>
    <div class="pct" style="right:12px;top:14px">15%</div>
  </section>

  <!-- special -->
  <section class="abs special">
    <h2>Special Price Discount <em>35%</em></h2>
    <p>Lorem ipsum dolor sit amet consectetur</p>
    <div class="cans" role="img" aria-label="Stack of canned dog food"></div>
  </section>

  <!-- filter -->
  <aside class="abs filter">
    <div class="head">Filter <svg width="16" height="14" viewBox="0 0 16 14" fill="none" stroke="#2a323c" stroke-width="1.4"><path d="M1 3h14M1 7h14M1 11h14"/><circle cx="10" cy="3" r="1.6" fill="#fff"/><circle cx="5" cy="7" r="1.6" fill="#fff"/><circle cx="11" cy="11" r="1.6" fill="#fff"/></svg></div>
    <h3>Price</h3>
    <div class="slider"><div class="fill"></div><div class="knob"></div></div>
    <div class="range"><span>£ 0.00</span><b>£ 89.50</b><span>£ 200.00</span></div>
    <h3 style="margin-top:56px">Popular Category</h3>
    <ul class="cats">
      <li>Dog</li>
      <li class="on">Cat</li>
      <li><ul><li>Wet food</li><li>Dry food</li><li>Vegetarian food</li></ul></li>
      <li>Holder</li>
    </ul>
  </aside>

  <!-- product grid -->
  <div class="abs pcard" style="top:676px;left:434px"><span class="new">NEW</span><span class="heart"><svg viewBox="0 0 12 12" fill="none" stroke="#0054AA" stroke-width="1.2"><path d="M6 10.5L1.6 6.2A2.6 2.6 0 016 2.6a2.6 2.6 0 014.4 3.6z"/></svg></span><div class="pack" role="img" aria-label="Bag of dog food" style="background:linear-gradient(180deg,#2d3d5a,#c9ccd6 60%,#e8eaf0)"></div><div class="stars">★★★★★</div><div class="name">Free-Run Chicken Wet Cat Food</div><div class="pp">£ 4.49 <span class="strike">£ 7.99</span></div><span class="btn">Add to Cart <svg viewBox="0 0 16 16" fill="none" stroke="#fff" stroke-width="1.3"><path d="M1 2h2l2 8h8l2-6H4"/><circle cx="6" cy="13" r="1"/><circle cx="12" cy="13" r="1"/></svg></span></div>
  <div class="abs pcard" style="top:676px;left:667px"><span class="heart"><svg viewBox="0 0 12 12" fill="none" stroke="#0054AA" stroke-width="1.2"><path d="M6 10.5L1.6 6.2A2.6 2.6 0 016 2.6a2.6 2.6 0 014.4 3.6z"/></svg></span><div class="pack" role="img" aria-label="Pouch of wet cat food" style="background:linear-gradient(180deg,#1d56b8,#2c74d8 50%,#e8edf6)"></div><div class="stars">★★★★★</div><div class="name">Free-Run Chicken Wet Cat Food</div><div class="pp">£ 4.49 <span class="strike">£ 7.99</span></div><span class="btn">Add to Cart <svg viewBox="0 0 16 16" fill="none" stroke="#fff" stroke-width="1.3"><path d="M1 2h2l2 8h8l2-6H4"/><circle cx="6" cy="13" r="1"/><circle cx="12" cy="13" r="1"/></svg></span></div>
  <div class="abs pcard" style="top:676px;left:901px"><span class="new">NEW</span><span class="heart"><svg viewBox="0 0 12 12" fill="none" stroke="#0054AA" stroke-width="1.2"><path d="M6 10.5L1.6 6.2A2.6 2.6 0 016 2.6a2.6 2.6 0 014.4 3.6z"/></svg></span><div class="pack" role="img" aria-label="Dark bag of dry pet food" style="background:linear-gradient(180deg,#3b3433,#584d4a 55%,#c9748b)"></div><div class="stars">★★★★★</div><div class="name">Free-Run Chicken Wet Cat Food</div><div class="pp">£ 4.49 <span class="strike">£ 7.99</span></div><span class="btn">Add to Cart <svg viewBox="0 0 16 16" fill="none" stroke="#fff" stroke-width="1.3"><path d="M1 2h2l2 8h8l2-6H4"/><circle cx="6" cy="13" r="1"/><circle cx="12" cy="13" r="1"/></svg></span></div>
  <div class="abs pcard" style="top:931px;left:434px"><span class="new">NEW</span><span class="heart"><svg viewBox="0 0 12 12" fill="none" stroke="#0054AA" stroke-width="1.2"><path d="M6 10.5L1.6 6.2A2.6 2.6 0 016 2.6a2.6 2.6 0 014.4 3.6z"/></svg></span><div class="pack" role="img" aria-label="Bag of dry cat food" style="background:linear-gradient(180deg,#f2f2f2,#c2a6c9 55%,#7e8591)"></div><div class="stars">★★★★★</div><div class="name">Free-Run Chicken Wet Cat Food</div><div class="pp">£ 4.49 <span class="strike">£ 7.99</span></div><span class="btn">Add to Cart <svg viewBox="0 0 16 16" fill="none" stroke="#fff" stroke-width="1.3"><path d="M1 2h2l2 8h8l2-6H4"/><circle cx="6" cy="13" r="1"/><circle cx="12" cy="13" r="1"/></svg></span></div>
  <div class="abs pcard" style="top:931px;left:667px"><span class="heart"><svg viewBox="0 0 12 12" fill="none" stroke="#0054AA" stroke-width="1.2"><path d="M6 10.5L1.6 6.2A2.6 2.6 0 016 2.6a2.6 2.6 0 014.4 3.6z"/></svg></span><div class="pack" role="img" aria-label="Bag of grain-free pet food" style="background:linear-gradient(180deg,#8a6a42,#6c2a2a 55%,#3d2020)"></div><div class="stars">★★★★★</div><div class="name">Free-Run Chicken Wet Cat Food</div><div class="pp">£ 4.49 <span class="strike">£ 7.99</span></div><span class="btn">Add to Cart <svg viewBox="0 0 16 16" fill="none" stroke="#fff" stroke-width="1.3"><path d="M1 2h2l2 8h8l2-6H4"/><circle cx="6" cy="13" r="1"/><circle cx="12" cy="13" r="1"/></svg></span></div>
  <div class="abs pcard" style="top:931px;left:901px"><span class="heart"><svg viewBox="0 0 12 12" fill="none" stroke="#0054AA" stroke-width="1.2"><path d="M6 10.5L1.6 6.2A2.6 2.6 0 016 2.6a2.6 2.6 0 014.4 3.6z"/></svg></span><div class="pack" role="img" aria-label="Bottle of pet supplement" style="background:linear-gradient(180deg,#e8eef6,#f7f9fc 40%,#2e5ea8)"></div><div class="stars">★★★★★</div><div class="name">Free-Run Chicken Wet Cat Food</div><div class="pp">£ 4.49 <span class="strike">£ 7.99</span></div><span class="btn">Add to Cart <svg viewBox="0 0 16 16" fill="none" stroke="#fff" stroke-width="1.3"><path d="M1 2h2l2 8h8l2-6H4"/><circle cx="6" cy="13" r="1"/><circle cx="12" cy="13" r="1"/></svg></span></div>

  <div class="abs pager">
    <span class="prev"><svg width="7" height="10" viewBox="0 0 7 10" fill="none" stroke="#fff" stroke-width="1.4"><path d="M5.5 1L1.5 5l4 4"/></svg></span>
    <span class="cur">1</span><span>2</span><span>...</span><span>6</span>
    <span><svg width="7" height="10" viewBox="0 0 7 10" fill="none" stroke="#8a929c" stroke-width="1.4"><path d="M1.5 1l4 4-4 4"/></svg></span>
  </div>

  <!-- offers -->
  <div class="abs tabs">
    <div class="t sep"><svg width="14" height="14" viewBox="0 0 14 14" fill="none" stroke="#2a323c" stroke-width="1.2"><rect x="1.5" y="5" width="11" height="8"/><path d="M1 5h12M7 5v8M7 5C5 1 2 3 4.5 5M7 5c2-4 5-2 2.5 0"/></svg>SPECIAL OFFERS</div>
    <div class="t b"><svg width="15" height="15" viewBox="0 0 15 15" fill="none" stroke="#0054AA" stroke-width="1.2"><circle cx="7.5" cy="7.5" r="6"/><path d="M5 10l5-5"/><circle cx="5.2" cy="5.2" r=".8"/><circle cx="9.8" cy="9.8" r=".8"/></svg>BIG DEALS PROMO</div>
    <div class="t b"><svg width="15" height="15" viewBox="0 0 15 15" fill="none" stroke="#0054AA" stroke-width="1.2"><circle cx="7.5" cy="7.5" r="6"/><circle cx="7.5" cy="7.5" r="3.5"/></svg>100% QUALITY</div>
    <div class="see" style="margin-top:-4px"><span>See All</span><svg width="7" height="12" viewBox="0 0 7 12" fill="none" stroke="#2a323c" stroke-width="1.4"><path d="M1 1l5 5-5 5"/></svg></div>
  </div>

  <section class="abs offer" style="top:1366px;left:84px;width:506px;height:418px">
    <div class="ph" role="img" aria-label="Wet pet food in a tin with a fork" style="background:linear-gradient(160deg,#7b736d 0%,#5a4e47 40%,#4a3a33 70%,#2e2623 100%)"></div>
    <div class="shade"></div>
    <div class="disc" style="left:415px;top:25px"><b>29%</b><small>DISCOUNT</small></div>
    <div class="abs" style="left:40px;top:240px"><span class="tag">ALIQUET PORTTITOR NISL</span></div>
    <h3 class="abs" style="left:40px;top:262px;font-size:37px">Natural Cat Treats</h3>
    <div class="abs op" style="left:40px;top:317px;font-size:19px">£ 4.49 <span style="margin-left:16px;text-decoration:line-through;color:#ddd">£ 7.99</span></div>
    <span class="btn abs" style="left:40px;top:354px;height:30px">Add to Cart <svg viewBox="0 0 16 16" fill="none" stroke="#fff" stroke-width="1.3"><path d="M1 2h2l2 8h8l2-6H4"/><circle cx="6" cy="13" r="1"/><circle cx="12" cy="13" r="1"/></svg></span>
  </section>

  <section class="abs offer" style="top:1366px;left:610px;width:244px;height:201px">
    <div class="ph" role="img" aria-label="Bowls of dry pet food and raw meat" style="background:linear-gradient(160deg,#9a7d5c,#7a3a2c 50%,#5a3f2b)"></div>
    <div class="shade"></div>
    <div class="pct" style="right:10px;top:14px">20%</div>
    <div class="abs" style="left:23px;top:96px"><span class="tag">ALIQUET PORTTITOR NISL</span></div>
    <h3 class="abs" style="left:23px;top:116px;font-size:21px">Natural Cat Treats</h3>
    <div class="abs op" style="left:23px;top:162px;font-size:15px">£ 5.99</div>
  </section>

  <section class="abs offer" style="top:1366px;left:874px;width:243px;height:201px">
    <div class="ph" role="img" aria-label="Bags of pet food with a bowl of kibble" style="background:linear-gradient(160deg,#b07b3e,#8a5a30 45%,#4b3526)"></div>
    <div class="shade"></div>
    <div class="pct" style="right:10px;top:14px">15%</div>
    <div class="abs" style="left:23px;top:90px"><span class="tag">ALIQUET PORTTITOR NISL</span></div>
    <h3 class="abs" style="left:23px;top:108px;font-size:21px;width:200px">Free-Run Chicken Wet Cat Food</h3>
    <div class="abs op" style="left:23px;top:164px;font-size:15px">£ 5.99</div>
  </section>

  <section class="abs offer" style="top:1584px;left:610px;width:507px;height:200px">
    <div class="ph" role="img" aria-label="Assorted bags of dry cat food on a shelf" style="background:linear-gradient(100deg,#4a6a8a,#2f3d57 35%,#3a4c7a 60%,#6a3a3a 85%,#a86a52)"></div>
    <div class="shade"></div>
    <div class="pct" style="right:14px;top:20px">5%</div>
    <div class="abs" style="left:23px;top:98px"><span class="tag">ALIQUET PORTTITOR NISL</span></div>
    <h3 class="abs" style="left:23px;top:120px;font-size:25px">Free-Run Chicken Wet Cat Food</h3>
    <div class="abs op" style="left:23px;top:162px;font-size:16px">£ 5.99</div>
  </section>

  <!-- brands -->
  <section class="abs brands">
    <h2>Shop By Brends</h2>
    <div class="sub">Thousends Of Products From Brands You Know And Trust</div>
    <div class="bgrid">
      <div>Carewell</div><div>GreenPaw</div><div>Regal Feline</div><div>Compass Pets</div><div>Bravura</div>
      <div>Wildroot</div><div>Pioneer Feed</div><div>Further</div><div>Evenkeel</div><div>Vantor</div>
    </div>
  </section>

  <!-- today's deals -->
  <div class="abs dhead"><span>TODAY'S DEALS</span><span class="see">See All <svg width="7" height="12" viewBox="0 0 7 12" fill="none" stroke="#2a323c" stroke-width="1.4" style="margin-top:4px"><path d="M1 1l5 5-5 5"/></svg></span></div>

  <div class="abs dcard" style="left:86px"><span class="heart"><svg viewBox="0 0 12 12" fill="none" stroke="#0054AA" stroke-width="1.2"><path d="M6 10.5L1.6 6.2A2.6 2.6 0 016 2.6a2.6 2.6 0 014.4 3.6z"/></svg></span><div class="pack" role="img" aria-label="Dark bag of dry pet food" style="background:linear-gradient(180deg,#3b3433,#584d4a 55%,#c9748b)"></div><div class="name">Free-Run Chicken Wet Cat Food</div><div class="pp">£ 4.49 <span class="strike">£ 7.99</span></div><span class="off">25% OFF</span></div>
  <div class="abs dcard" style="left:260px"><span class="heart"><svg viewBox="0 0 12 12" fill="none" stroke="#0054AA" stroke-width="1.2"><path d="M6 10.5L1.6 6.2A2.6 2.6 0 016 2.6a2.6 2.6 0 014.4 3.6z"/></svg></span><div class="pack" role="img" aria-label="Bag of dog food" style="background:linear-gradient(180deg,#2d3d5a,#c9ccd6 60%,#e8eaf0)"></div><div class="name">Free-Run Chicken Wet Cat Food</div><div class="pp">£ 4.49 <span class="strike">£ 7.99</span></div><span class="off">25% OFF</span></div>
  <div class="abs dcard" style="left:434px"><span class="heart"><svg viewBox="0 0 12 12" fill="none" stroke="#0054AA" stroke-width="1.2"><path d="M6 10.5L1.6 6.2A2.6 2.6 0 016 2.6a2.6 2.6 0 014.4 3.6z"/></svg></span><div class="pack" role="img" aria-label="Bag of dry cat food" style="background:linear-gradient(180deg,#f2f2f2,#c2a6c9 55%,#7e8591)"></div><div class="name">Free-Run Chicken Wet Cat Food</div><div class="pp">£ 4.49 <span class="strike">£ 7.99</span></div><span class="off">25% OFF</span></div>
  <div class="abs dcard" style="left:610px"><span class="heart"><svg viewBox="0 0 12 12" fill="none" stroke="#0054AA" stroke-width="1.2"><path d="M6 10.5L1.6 6.2A2.6 2.6 0 016 2.6a2.6 2.6 0 014.4 3.6z"/></svg></span><div class="pack" role="img" aria-label="Pouch of wet cat food" style="background:linear-gradient(180deg,#1d56b8,#2c74d8 50%,#e8edf6)"></div><div class="name">Free-Run Chicken Wet Cat Food</div><div class="pp">£ 4.49 <span class="strike">£ 7.99</span></div><span class="off">25% OFF</span></div>
  <div class="abs dcard" style="left:786px"><span class="heart"><svg viewBox="0 0 12 12" fill="none" stroke="#0054AA" stroke-width="1.2"><path d="M6 10.5L1.6 6.2A2.6 2.6 0 016 2.6a2.6 2.6 0 014.4 3.6z"/></svg></span><div class="pack" role="img" aria-label="Dark bag of dry pet food" style="background:linear-gradient(180deg,#3b3433,#584d4a 55%,#c9748b)"></div><div class="name">Free-Run Chicken Wet Cat Food</div><div class="pp">£ 4.49 <span class="strike">£ 7.99</span></div><span class="off">25% OFF</span></div>
  <div class="abs dcard" style="left:961px"><span class="heart"><svg viewBox="0 0 12 12" fill="none" stroke="#0054AA" stroke-width="1.2"><path d="M6 10.5L1.6 6.2A2.6 2.6 0 016 2.6a2.6 2.6 0 014.4 3.6z"/></svg></span><div class="pack" role="img" aria-label="Bottle of pet supplement" style="background:linear-gradient(180deg,#e8eef6,#f7f9fc 40%,#2e5ea8)"></div><div class="name">Free-Run Chicken Wet Cat Food</div><div class="pp">£ 4.49 <span class="strike">£ 7.99</span></div><span class="off">25% OFF</span></div>

  <div class="abs arrow" style="left:66px"><svg width="8" height="12" viewBox="0 0 8 12" fill="none" stroke="#2a323c" stroke-width="1.5"><path d="M6 1L1.5 6 6 11"/></svg></div>
  <div class="abs arrow" style="left:1099px"><svg width="8" height="12" viewBox="0 0 8 12" fill="none" stroke="#2a323c" stroke-width="1.5"><path d="M2 1l4.5 5L2 11"/></svg></div>

  <!-- about -->
  <section class="abs about">
    <div class="video" role="img" aria-label="Woman hugging a large white dog beside a bag of puppy food">
      <div class="play"><svg width="18" height="20" viewBox="0 0 18 20"><path d="M2 1l15 9-15 9z" fill="#fff"/></svg></div>
    </div>
    <h2>About Quill Pet</h2>
    <p>Lorem ipsum dolor sit amet consectetur. Lectus erat posuere diam sed nunc. Amet proin sapien phasellus eget amet cursus nulla. A vitae eu integer posuere nunc etiam urna proin. Libero turpis tincidunt nullam quis aliquam nibh. Ut ut a netus elit egestas amet fames risus venenatis. Eu ultrices dui neque lectus varius ornare sit nibh tellus.</p>
    <span class="more">Read More</span>
  </section>

  <!-- footer -->
  <div class="abs brand" style="top:3066px;left:84px"><i class="dot"></i><span>Quill Pet Shop</span></div>
  <div class="abs fcontact">
    <div class="row"><svg viewBox="0 0 16 16" fill="none" stroke="#2a323c" stroke-width="1.3"><path d="M8 15s5-5 5-9A5 5 0 003 6c0 4 5 9 5 9z"/><circle cx="8" cy="6" r="1.8"/></svg><span>48 Maple Row, Fairview,<br>Ohio 44102</span></div>
    <div class="row"><svg viewBox="0 0 16 16" fill="none" stroke="#2a323c" stroke-width="1.3"><path d="M3 2h3l1.5 3.5-2 1.3a8 8 0 004 4l1.3-2L14 10v3a1 1 0 01-1 1A12 12 0 012 3a1 1 0 011-1z"/></svg><span>(555) 014-2280</span></div>
    <div class="row"><svg viewBox="0 0 16 16" fill="none" stroke="#2a323c" stroke-width="1.3"><path d="M8 15s5-5 5-9A5 5 0 003 6c0 4 5 9 5 9z"/><circle cx="8" cy="6" r="1.8"/></svg><span>hello@quillpet.example</span></div>
  </div>
  <div class="abs fcol" style="left:349px"><h4>Quick Links</h4><a>Blog</a><a>New Items Just In!</a><a>Reviews</a><a>My Account</a><a>Brand Ambassadors</a></div>
  <div class="abs fcol" style="left:524px"><h4>About</h4><a>Privacy Policy</a><a>Terms &amp; Conditions</a><a>About Us</a></div>
  <div class="abs fcol" style="left:699px"><h4>Customer Service</h4><a>Delivery</a><a>Contact</a><a>Returns</a><a>Wishlist</a></div>
  <div class="abs fcol" style="left:912px">
    <h4>Support Paymants</h4>
    <div class="pay"><span>CardOne</span><span>Vistra</span><span>Meridian</span><span>Paywell</span></div>
    <h4>Media Social</h4>
    <div class="social"><span>Linkly</span><span>Peeper</span><span>Pictor</span><span>Workwise</span></div>
  </div>
  <div class="abs copy">Copyright © 2023 Quill Pet. All Right Reserved.</div>

</div>
</body>
</html>
```